Letter Head- Window Cleaning Industry

Need a letter head for 'Fernbrook Window Cleaning'. We provide a premium residential & commercial window cleaning service to Melbourne and surrounding suburbs.
Would like a design similar to the flyer, logo and uniform attached. The final design should communicate trust and quality.
Address is 1204/58 Haldane St, Southmere Victoria 3141. The rest of the information is on the flyer.
*Please note the Phone number on the uniform designs is incorrect.

Thank-you very much!

Industry/Entity Type

Window Cleaning

```html
<!DOCTYPE html>
<html lang="en">
<head>
<meta charset="utf-8">
<title>Fernbrook Window Cleaning – Stationery</title>
<link rel="stylesheet" href="https://fonts.googleapis.com/css2?family=Open+Sans:wght@400;600;700&display=swap">
<style>
:root{
  --bg:#3b3b3b;
  --paper:#ffffff;
  --orange:#f39019;
  --ink:#3a3a3a;
  --grey:#8a8a8a;
  --block:#5a5a5a;
  --skyline:#e4e4e6;
  --window:#9a9a9c;
}
*{box-sizing:border-box;margin:0;padding:0}
html,body{width:1200px;height:843px;overflow:hidden;background:var(--bg);font-family:"Open Sans",Arial,sans-serif}
.stage{position:relative;width:1200px;height:843px}

/* Shared brand mark */
.brand{display:flex;align-items:center;gap:6px}
.brand-square{width:14px;height:14px;background:var(--orange)}
.brand-name{font-weight:700;color:var(--ink);white-space:nowrap}

.skyline{position:absolute;left:0;right:0;bottom:0;background:linear-gradient(to top,var(--skyline),rgba(228,228,230,.2))}

/* Envelope */
.envelope{position:absolute;left:45px;top:360px;width:505px;height:290px;background:var(--paper);box-shadow:0 4px 14px rgba(0,0,0,.35);overflow:hidden}
.envelope-band{position:absolute;top:18px;right:0;width:78%;height:30px;background:linear-gradient(to left,var(--orange) 35%,rgba(243,144,25,0))}
.envelope-block{position:absolute;left:0;top:92px;width:10px;height:32px;background:var(--block)}
.envelope .brand{position:absolute;left:24px;top:98px}
.envelope .brand-name{font-size:15px}
.envelope-window{position:absolute;left:283px;top:120px;width:190px;height:96px;border-radius:12px;background:var(--window)}
.envelope .skyline{height:90px}

/* Letterhead */
.letterhead{position:absolute;left:580px;top:30px;width:560px;height:790px;background:var(--paper);box-shadow:0 4px 14px rgba(0,0,0,.35);overflow:hidden}
.letterhead-band{position:absolute;left:0;top:86px;width:62%;height:28px;background:linear-gradient(to right,var(--orange) 40%,rgba(243,144,25,0))}
.letterhead-block{position:absolute;right:0;top:76px;width:14px;height:28px;background:var(--block)}
.letterhead .brand{position:absolute;right:30px;top:86px}
.letterhead .brand-name{font-size:15px}
.letter-body{position:absolute;left:78px;top:178px;width:430px;color:var(--ink)}
.letter-title{font-size:11px;font-weight:700;color:var(--grey);margin-bottom:10px;letter-spacing:.2px}
.letter-body p{font-size:8.4px;line-height:1.38;text-align:justify;margin-bottom:11px}
.signature{position:absolute;left:272px;top:608px;width:110px;height:40px;background:linear-gradient(to right,rgba(110,90,160,.12),rgba(110,90,160,.3),rgba(110,90,160,.1));border-radius:20px}
.seal{position:absolute;left:364px;top:566px;width:108px;height:108px;border-radius:50%;background:rgba(120,100,170,.25)}
.letterhead .skyline{height:100px}
.letter-footer{position:absolute;left:34px;right:20px;bottom:26px;display:flex;font-size:6.6px;line-height:1.45;color:var(--ink)}
.footer-col{padding:0 12px;border-left:1px solid var(--ink)}
.footer-col:first-child{border-left:0;padding-left:0}
.footer-col.abn{margin-left:auto;border-left:0;padding-right:0}
</style>
</head>
<body>
<main class="stage">

  <section class="envelope" aria-label="Envelope">
    <div class="envelope-band"></div>
    <div class="envelope-block"></div>
    <div class="brand"><span class="brand-square"></span><span class="brand-name">Fernbrook Window Cleaning</span></div>
    <div class="envelope-window"></div>
    <div class="skyline" role="img" aria-label="Faint grey city skyline silhouette"></div>
  </section>

  <section class="letterhead" aria-label="Letterhead">
    <div class="letterhead-band"></div>
    <div class="letterhead-block"></div>
    <div class="brand"><span class="brand-square"></span><span class="brand-name">Fernbrook Window Cleaning</span></div>

    <article class="letter-body">
      <h2 class="letter-title">SAMPLE TEXT HERE</h2>
      <p>Lorem ipsum dolor sit amet, consectetuer adipiscing elit. Pellentesque tristique elementum sem. Quisque eget erat ac lectus sodales faucibus. Nam commodo est. Cras consequat faucibus velit. Nam ac magna. Sed et ligula. Nam volutpat, elit ac facilisis tempor, neque augue euismod leo, sit amet molestie sem est eu libero. Nulla facilisi. Pellentesque sit amet odio. Curabitur a leo consectetuer leo blandit porttitor. Pellentesque velit quam, gravida at, pharetra eu, convallis non, sem. Aenean tempor nibh at purus. Pellentesque porta. Suspendisse congue, lacus sit amet imperdiet imperdiet, urna massa rutrum urna, id elementum tellus diam quis risus.</p>
      <p>In dui turpis, varius vitae, tincidunt id, consequat ut, leo. Donec tincidunt tristique odio. Nulla erat felis, euismod nec, fringilla non, aliquet et, magna. Nulla at magna quis nisl pretium vehicula. Pellentesque habitant morbi tristique senectus et netus et malesuada fames ac turpis egestas. Class aptent taciti sociosqu ad litora torquent per conubia nostra, per inceptos himenaeos. In vel quam. Phasellus varius convallis purus. In non turpis. Nam sed risus. Etiam non neque at nisl gravida porttitor. Donec leo dolor, feugiat ut, pharetra et, porttitor a, metus. Suspendisse laoreet magna vel elit. Ut est augue, fermentum ac, molestie at, vestibulum et, urna.</p>
      <p>Nunc purus. Cras auctor. In ornare neque id ipsum. Nulla tincidunt, diam sit amet viverra euismod, sapien augue fringilla neque, at pellentesque felis tortor vel enim. Etiam dignissim. Sed a tortor vel nisi euismod ultricies. Donec molestie congue lectus. Integer sed turpis a tortor imperdiet consequat. Maecenas molestie placerat urna. Sed pede enim, sollicitudin nec, pretium nec, sollicitudin a, felis. In hac habitasse platea dictumst. Nam facilisis, tellus non scelerisque placerat, turpis turpis semper ante, euismod imperdiet augue nisi et neque. Vivamus tincidunt.</p>
      <p>Nulla lobortis ultricies nulla. Pellentesque purus mi, consequat quis, hendrerit sed, imperdiet non, eros. Nullam urna est, vehicula nec, cursus nec, dignissim sit amet, risus. Duis molestie, tellus sit amet laoreet ullamcorper, urna nisi fringilla ante, at rhoncus justo dolor vel dui. Nam hendrerit luctus lorem. Aenean tempor, metus vel posuere gravida, arcu nunc imperdiet tellus, ut blandit sem magna a turpis. Vivamus in neque. Lorem ipsum dolor sit amet, consectetuer adipiscing elit. Duis tristique tortor id nisl feugiat posuere. Maecenas posuere nisi ac risus. Nunc hendrerit. Praesent porta tempus ligula. Morbi in leo. Curabitur sapien nulla, cursus eget, faucibus in, porttitor et, odio. Praesent sed justo sed arcu commodo feugiat. Duis facilisis nulla ut eros. Cras libero. Donec mollis consectetuer metus. Praesent odio.</p>
    </article>

    <div class="signature" role="img" aria-label="Handwritten signature"></div>
    <div class="seal" role="img" aria-label="Round company stamp"></div>

    <div class="skyline" role="img" aria-label="Faint grey city skyline silhouette"></div>

    <footer class="letter-footer">
      <div class="footer-col">Daniel R. Fernbrook<br>1204/58 Haldane St, Southmere Victoria 3141</div>
      <div class="footer-col">Telephone: (03) 5550 1427<br>Facsimile: &nbsp;xxxx xx xx</div>
      <div class="footer-col">E-mail: info@fernbrookwindows.com.au<br>Website: www.fernbrookwindows.com.au</div>
      <div class="footer-col abn">ABN No: &nbsp;41 508 922 316</div>
    </footer>
  </section>

</main>
</body>
</html>
```